Bref créative
Norland Equity Partners
Investing
Professional
Tom Radcliffe
President
728 Maplewood Ave. Suite 310
Oak Terrace, CA 90418
tom@NorlandEquityPartners.com
www.NorlandEquityPartners.com
We want our logo to be the main component of the card. Have fun and let me see what you got!
Feel free to try 1 or 2 sided card ideas.
Can use other fonts besides the logo font if you desire.

```html
<!DOCTYPE html>
<html lang="en">
<head>
<meta charset="utf-8">
<title>Norland Equity Partners – Business Card</title>
<link href="https://fonts.googleapis.com/css2?family=Montserrat:wght@400;600;700&display=swap" rel="stylesheet">
<style>
  :root {
    --backdrop: #1d1d1d;
    --brand-red: #e8171b;
    --card-white: #ffffff;
    --ink: #222222;
    --ink-soft: #555555;
    --rule: #9a9a9a;
  }
  * { margin: 0; padding: 0; box-sizing: border-box; }
  html, body {
    width: 1200px; height: 901px; overflow: hidden;
    background: var(--backdrop);
    font-family: "Montserrat", Arial, sans-serif;
  }
  .stage { position: relative; width: 1200px; height: 901px; }
  .card {
    position: absolute; top: 336px;
    width: 394px; height: 226px; border-radius: 12px;
  }
  .card-front { left: 195px; background: var(--card-white); }
  .card-back { left: 613px; background: var(--brand-red); color: var(--card-white); }

  .holder {
    position: absolute; top: 46px; left: 0; width: 100%;
    text-align: center; font-size: 14px; font-weight: 700; color: var(--ink);
  }
  .holder-name { color: var(--brand-red); }
  .holder-sep { margin: 0 6px; }

  .front-brand {
    position: absolute; left: 22px; top: 96px; width: 186px;
    display: flex; flex-direction: column; align-items: center; gap: 8px;
  }
  .brand-dot { width: 40px; height: 40px; border-radius: 50%; background: var(--brand-red); }
  .front-brand .brand-name {
    font-size: 10px; font-weight: 600; letter-spacing: 1.5px;
    color: var(--ink); text-transform: uppercase; text-align: center; line-height: 1.4;
  }

  .divider {
    position: absolute; left: 214px; top: 94px; width: 1px; height: 70px;
    background: var(--rule);
  }
  .contact {
    position: absolute; left: 224px; top: 96px; list-style: none;
    font-size: 8.5px; color: var(--ink-soft); line-height: 13px;
  }
  .contact li { display: flex; align-items: center; gap: 5px; white-space: nowrap; }
  .contact svg { width: 8px; height: 8px; fill: var(--brand-red); flex: none; }
  .contact .indent { padding-left: 13px; }

  .back-brand {
    position: absolute; top: 48px; left: 0; width: 100%;
    display: flex; flex-direction: column; align-items: center;
  }
  .back-brand .brand-dot { background: var(--card-white); width: 46px; height: 46px; }
  .back-brand .brand-name {
    margin-top: 10px; padding-bottom: 6px; width: 250px;
    border-bottom: 1px solid var(--card-white);
    font-size: 13px; font-weight: 600; letter-spacing: 2.5px;
    text-transform: uppercase; text-align: center;
  }
  .web {
    position: absolute; top: 178px; left: 0; width: 100%;
    text-align: center; font-size: 12px; font-weight: 700; letter-spacing: 1px;
  }
</style>
</head>
<body>
<main class="stage">
  <section class="card card-front">
    <p class="holder"><span class="holder-name">Tom Radcliffe</span><span class="holder-sep">|</span>President</p>

    <div class="front-brand">
      <span class="brand-dot"></span>
      <span class="brand-name">Norland Equity Partners</span>
    </div>

    <span class="divider"></span>

    <ul class="contact">
      <li><svg viewBox="0 0 10 10"><path d="M5 0C3 0 1.5 1.5 1.5 3.5 1.5 6 5 10 5 10s3.5-4 3.5-6.5C8.5 1.5 7 0 5 0zm0 5a1.5 1.5 0 1 1 0-3 1.5 1.5 0 0 1 0 3z"/></svg>728 Maplewood Ave. Suite 310</li>
      <li class="indent">Oak Terrace, CA 90418</li>
      <li><svg viewBox="0 0 10 10"><path d="M2 0l2 2.5-1 1.5c.8 1.4 1.6 2.2 3 3l1.5-1L10 8l-1.5 2C4 9.5.5 6 0 1.5z"/></svg>310-555-0147</li>
      <li><svg viewBox="0 0 10 10"><path d="M0 2h10v6H0zm1 .8v.4L5 6l4-2.8v-.4z"/></svg>tom@NorlandEquityPartners.com</li>
      <li><svg viewBox="0 0 10 10"><circle cx="5" cy="5" r="4.5"/></svg>www.NorlandEquityPartners.com</li>
    </ul>
  </section>

  <section class="card card-back">
    <div class="back-brand">
      <span class="brand-dot"></span>
      <span class="brand-name">Norland Equity Partners</span>
    </div>
    <p class="web">www.NorlandEquityPartners.com</p>
  </section>
</main>
</body>
</html>
```